Redesign of business card for Birchline Mechanical

We are looking for a new design for our business cards for Birchline Mechanical. We are a plumbing & HVAC construction company, operating on the West Coast of Canada and USA. Logo attached.
Industry/Entity Type
Construction - Plumbing & HVAC
Contact Information for Business Card
Name, address, phone numbers, email, website address
Look and feel
Each slider illustrates characteristics of the customer's brand and the style your logo design should communicate.

```html
<!DOCTYPE html>
<html lang="en">
<head>
<meta charset="utf-8">
<title>Birchline Mechanical – Business Card</title>
<link rel="stylesheet" href="https://fonts.googleapis.com/css2?family=Roboto:wght@400;700&display=swap">
<style>
  :root {
    --bg: #5b6370;
    --ink: #1b1b1b;
    --paper: #ffffff;
    --grey: #9a9a9a;
    --grey-light: #c9c9c9;
    --panel-line: #bdbdbd;
  }
  * { margin: 0; padding: 0; box-sizing: border-box; }
  html, body { width: 1200px; height: 900px; overflow: hidden; }
  body {
    background: var(--bg);
    font-family: "Roboto", Arial, sans-serif;
    position: relative;
  }
  .card {
    position: absolute;
    left: 280px;
    width: 640px;
    height: 366px;
    background: var(--ink);
    overflow: hidden;
    box-shadow: 0 8px 24px rgba(0,0,0,.35);
  }
  .card--front { top: 50px; }
  .card--back { top: 466px; }
  .card svg.art { position: absolute; inset: 0; }

  .brand {
    position: absolute;
    display: flex;
    align-items: center;
    gap: 10px;
    font-weight: 700;
    font-size: 22px;
    letter-spacing: .04em;
    text-transform: uppercase;
  }
  .brand__mark { width: 18px; height: 18px; flex: none; }
  .card--front .brand { left: 200px; top: 128px; color: var(--paper); }
  .card--front .brand__mark { background: var(--paper); }
  .card--back .brand {
    left: 32px; top: 56px;
    width: 190px;
    color: var(--ink);
    font-size: 20px;
    line-height: 1.2;
  }
  .card--back .brand__mark { background: var(--ink); width: 22px; height: 22px; }

  .contact-panel {
    position: absolute;
    left: 300px; top: 40px;
    width: 312px; height: 290px;
    border: 1.5px solid var(--panel-line);
    border-radius: 14px;
    background: rgba(255,255,255,.06);
    padding: 22px 22px;
    text-align: right;
  }
  .person__name { font-weight: 700; font-size: 30px; color: var(--grey); line-height: 1.1; }
  .person__role { font-size: 16px; color: var(--paper); margin-top: 2px; }
  .contact-list {
    list-style: none;
    margin-top: 58px;
    color: var(--paper);
    font-size: 15px;
    line-height: 1.5;
  }
  .contact-list li { display: flex; justify-content: flex-end; align-items: flex-start; gap: 10px; }
  .contact-list svg { width: 14px; height: 14px; margin-top: 4px; flex: none; fill: var(--grey-light); }
</style>
</head>
<body>

<section class="card card--front" aria-label="Card front">
  <svg class="art" viewBox="0 0 640 366" width="640" height="366">
    <defs>
      <linearGradient id="flagTone" x1="0" y1="0" x2="1" y2="1">
        <stop offset="0" stop-color="#d9d9d9"/>
        <stop offset="1" stop-color="#8f8f8f"/>
      </linearGradient>
    </defs>
    <polygon points="0,0 440,0 0,150" fill="url(#flagTone)" role="img" aria-label="Greyscale flag with stars and stripes"/>
    <polygon points="170,366 640,366 640,140" fill="url(#flagTone)" role="img" aria-label="Greyscale mountain range over flag stripes"/>
  </svg>
  <div class="brand"><span class="brand__mark"></span><span class="brand__name">Birchline Mechanical</span></div>
</section>

<section class="card card--back" aria-label="Card back">
  <svg class="art" viewBox="0 0 640 366" width="640" height="366">
    <polygon points="0,0 310,0 190,366 0,366" fill="var(--paper)"/>
  </svg>
  <div class="brand"><span class="brand__mark"></span><span class="brand__name">Birchline Mechanical</span></div>

  <div class="contact-panel">
    <p class="person__name">Your full Name</p>
    <p class="person__role">CEO</p>
    <ul class="contact-list">
      <li>+123 456 7890
        <svg viewBox="0 0 24 24"><path d="M6.6 10.8a15 15 0 0 0 6.6 6.6l2.2-2.2c.3-.3.7-.4 1-.2 1.1.4 2.3.6 3.6.6.6 0 1 .4 1 1V20c0 .6-.4 1-1 1A17 17 0 0 1 3 4c0-.6.4-1 1-1h3.5c.6 0 1 .4 1 1 0 1.3.2 2.5.6 3.6.1.3 0 .7-.2 1z"/></svg></li>
      <li>info@birchlinemechanical.com
        <svg viewBox="0 0 24 24"><path d="M2 5h20v14H2zm2 2v.5l8 5 8-5V7l-8 5z"/></svg></li>
      <li>www.birchlinemechanical.com
        <svg viewBox="0 0 24 24"><path d="M12 2a10 10 0 1 0 0 20 10 10 0 0 0 0-20zm7.9 9h-3.9a15 15 0 0 0-1.4-6.3A8 8 0 0 1 19.9 11zM12 4c1 1.4 1.9 4 2 7h-4c.1-3 1-5.6 2-7zM9.4 4.7A15 15 0 0 0 8 11H4.1a8 8 0 0 1 5.3-6.3zM4.1 13H8a15 15 0 0 0 1.4 6.3A8 8 0 0 1 4.1 13zM12 20c-1-1.4-1.9-4-2-7h4c-.1 3-1 5.6-2 7zm2.6-.7A15 15 0 0 0 16 13h3.9a8 8 0 0 1-5.3 6.3z"/></svg></li>
      <li>your address your address your<br>address your address
        <svg viewBox="0 0 24 24"><path d="M12 2a7 7 0 0 0-7 7c0 5 7 13 7 13s7-8 7-13a7 7 0 0 0-7-7zm0 9.5a2.5 2.5 0 1 1 0-5 2.5 2.5 0 0 1 0 5z"/></svg></li>
    </ul>
  </div>
</section>

</body>
</html>
```